Flyer Design for Kestrel Vale Lodgings

We are seeking a skilled and creative designer to create a visually appealing and informative flyer for Kestrel Vale Lodgings (KVL). This flyer will be distributed to condo owners in Toronto, introducing our comprehensive management services for their properties. The primary goal of the flyer is to attract condo owners to avail our services and highlight the benefits of partnering with Kestrel Vale Lodgings for their property management needs.
Size: 8.5 x 11 inches - single sided
Scope of the Project:
- Design Concept: Develop a visually striking and professional design concept that aligns with Kestrel Vale Lodgings' brand identity. The design should be modern, clean, and convey a sense of reliability and expertise in property management.
- Layout and Content: Create an engaging layout that effectively communicates the key features and benefits of our management services. The content should be concise, informative, and persuasive. The following points should be included:
a. Service Offering: Clearly state that Kestrel Vale Lodgings specializes in property management services for condo owners in Toronto.
b. Fee Structure: Highlight our competitive pricing model, which includes a management fee of 15% plus tax of the pure rent we manage to secure for the property.
c. Rental Marketing: Emphasize our comprehensive approach to rental marketing by showcasing that we list the unit on our own website, as well as other booking engines such as Nestvora, QLMX, and other similar platforms (not limited to these).
d. Target Market: Emphasize that Kestrel Vale Lodgings specializes in securing one-month minimum executive rentals. However, highlight that we also manage units with short-term rental (STR) permits and can effectively market their properties for durations shorter than one month.
- Visual Elements: Incorporate high-quality images of stylish and well-maintained apartments to visually represent the type of properties we manage. The images should be appealing and complement the overall design.
- Contact Information: Clearly display our contact information, including phone number, email address, and website URL, to encourage interested condo owners to reach out to us.
- Design Variations: Provide the flyer design in multiple file formats (e.g., PDF, JPEG, PNG) to accommodate both digital distribution and printing purposes.
Additional Guidelines:
- Maintain consistency with Kestrel Vale Lodgings' brand colors and logo, ensuring a cohesive visual identity.
- Ensure that the design is easy to read and understand, using legible fonts and appropriate font sizes.
- Make effective use of white space and other design elements to create an aesthetically pleasing layout.
- Proofread the content for accuracy, grammar, and spelling errors.
Feel free to contact us if you have any questions or require further clarification during the design process. We appreciate your attention to detail and creativity in helping us create an impactful flyer for Kestrel Vale Lodgings.
Thank you for your interest, and we look forward to reviewing your design proposal!
PS: attached is our company logo.
Here's a small inspiration that you can use:
Section 1: Introduction
Discover stress-free property management solutions for your furnished properties in Toronto.
Section 2: Full Management Services
Leave the Hassle to Us!
At Kestrel Vale Lodgings, we offer comprehensive full management services for your furnished properties. Our dedicated team takes care of all the details, ensuring a seamless and hands-free experience for you and your guests.
Section 3: Why Choose Kestrel Vale Lodgings?
Experience the Benefits:
1. Time and Convenience: We handle all aspects of property management, from tenant screening and lease agreements to maintenance requests and rent collection. Relax and let us take care of it all!
2. Maximizing Returns: Our team is committed to maximizing your rental income, while minimizing vacancies. We use strategic marketing techniques to attract qualified tenants and optimize rental rates.
3. Industry Connections: Benefit from our extensive network of industry professionals. We collaborate with photographers, cleaners, and maintenance providers to ensure your property always looks its best with minimum costs.
Section 4: Our Approach
Customized Solutions for Your Property:
1. Property Marketing: We leverage our expertise to market your property effectively. We list your unit on our own website (kestrelvalelodgings.example) and other popular booking platforms, attracting a wide range of potential tenants.
2. Tenant Screening: Our rigorous tenant screening process ensures that only qualified and reliable individuals occupy your property. Your peace of mind is our priority.
3. Rental Management: From managing inquiries and scheduling viewings to handling lease agreements and rent collection, we oversee every aspect of the rental process.
Section 5: Contact Us
Ready to Partner with Us?
Experience the benefits of stress-free property management. Contact Kestrel Vale Lodgings today to learn more about our full management services for furnished properties in Toronto.
Phone: [Insert Phone Number] Email: [Insert Email Address] Website: [Insert Website URL] QR Code: [Insert QR Code]
Make the 15% plus tax management fee obvious
Property Management and Executive Rentals

```html
<!DOCTYPE html>
<html lang="en">
<head>
<meta charset="utf-8">
<title>Kestrel Vale Lodgings – Flyer</title>
<link rel="stylesheet" href="https://fonts.googleapis.com/css2?family=Libre+Baskerville:wght@700&family=Montserrat:wght@400;500;700&display=swap">
<style>
:root{
  --teal-deep:#0e3f4f;
  --teal-mid:#1d5566;
  --teal-soft:#2b6d7c;
  --teal-brand:#5aa09f;
  --gold:#c89a2e;
  --gold-text:#e9b74a;
  --gold-dark:#9a7322;
  --ink:#1c1c1c;
  --paper:#ffffff;
  --backdrop:#d7d7da;
}
*{margin:0;padding:0;box-sizing:border-box}
html,body{width:755px;height:1200px;overflow:hidden;background:var(--backdrop)}
body{font-family:'Montserrat',sans-serif;position:relative}
.flyer{position:absolute;left:17px;top:90px;width:720px;height:1020px;background:var(--paper);overflow:hidden;box-shadow:0 6px 18px rgba(0,0,0,.25)}
.flyer-shapes{position:absolute;left:0;top:0;width:720px;height:1020px}
.brand-name{position:absolute;left:24px;top:120px;width:150px;text-align:center;color:var(--teal-brand);font-weight:500;font-size:15px;letter-spacing:1.5px;line-height:1.35;text-transform:uppercase}
.headline{position:absolute;left:0;top:532px;width:720px;text-align:center;color:#fff;font-family:'Libre Baskerville',serif;font-weight:700;font-size:29px;line-height:41px}
.services-pill{position:absolute;left:219px;top:641px;width:282px;height:29px;border-radius:7px;background:var(--gold);color:#fff;font-size:16px;text-align:center;line-height:29px}
.services-pill strong{font-weight:700;font-size:18px}
.service-cell{position:absolute;color:#fff;font-size:12px;line-height:16.8px;padding:0 18px 0 26px}
.service-cell b.label{color:var(--gold-text);font-weight:700;font-size:14px}
.service-cell strong{font-weight:700}
.cell-offering{left:0;top:694px;width:360px}
.cell-fee{left:360px;top:692px;width:360px;padding-left:18px}
.cell-marketing{left:0;top:780px;width:360px}
.cell-market{left:360px;top:776px;width:360px;padding-left:18px}
.contact-tab{position:absolute;left:271px;top:917px;width:179px;height:21px;background:var(--teal-deep);color:#fff;font-size:13px;text-align:center;line-height:21px;border-radius:3px}
.contact-phone{position:absolute;left:0;top:950px;width:720px;text-align:center;color:var(--gold-dark);font-size:23px;font-weight:500;display:flex;justify-content:center;align-items:center;gap:6px}
.contact-lines{position:absolute;left:0;top:985px;width:720px;display:flex;justify-content:center;gap:30px;font-size:12.5px;color:var(--ink)}
.contact-lines span{display:flex;align-items:center;gap:5px}
</style>
</head>
<body>
<main class="flyer">
  <svg class="flyer-shapes" viewBox="0 0 720 1020" xmlns="http://www.w3.org/2000/svg">
    <defs>
      <linearGradient id="roomTone" x1="0" y1="0" x2="1" y2="1">
        <stop offset="0" stop-color="#c9ccd0"/>
        <stop offset=".5" stop-color="#e3e4e6"/>
        <stop offset="1" stop-color="#7d7f83"/>
      </linearGradient>
      <linearGradient id="roundTone" x1="0" y1="0" x2="0" y2="1">
        <stop offset="0" stop-color="#eceef0"/>
        <stop offset="1" stop-color="#a9a39a"/>
      </linearGradient>
    </defs>
    <!-- interior photograph area -->
    <rect role="img" aria-label="Photo of a bright furnished loft apartment with living area and kitchen" x="0" y="0" width="720" height="560" fill="url(#roomTone)"/>
    <!-- white corner for brand -->
    <path d="M0,0 L371,0 Q230,120 90,210 Q40,240 0,242 Z" fill="var(--paper)"/>
    <path d="M371,0 Q230,120 90,210 Q40,240 0,242" fill="none" stroke="var(--gold)" stroke-width="3"/>
    <!-- deep teal band -->
    <path d="M0,520 Q180,500 360,480 Q540,500 720,520 L720,927 L0,927 Z" fill="var(--gold)"/>
    <path d="M0,527 Q180,507 360,487 Q540,507 720,527 L720,927 L0,927 Z" fill="var(--teal-deep)"/>
    <!-- service grid -->
    <rect x="0" y="686" width="360" height="82" fill="var(--teal-soft)"/>
    <rect x="360" y="686" width="360" height="82" fill="var(--teal-mid)"/>
    <rect x="0" y="768" width="360" height="132" fill="var(--teal-mid)"/>
    <rect x="360" y="768" width="360" height="132" fill="var(--teal-soft)"/>
    <!-- headline rule -->
    <line x1="93" y1="622" x2="628" y2="622" stroke="var(--gold)" stroke-width="1.5"/>
    <!-- contact band divider -->
    <line x1="0" y1="927" x2="720" y2="927" stroke="var(--gold)" stroke-width="2"/>
    <!-- round photos -->
    <circle cx="144" cy="425" r="102" fill="var(--gold)"/>
    <circle role="img" aria-label="Photo of a dining table in a sunlit apartment" cx="144" cy="425" r="96" fill="url(#roundTone)"/>
    <circle cx="360" cy="363" r="110" fill="var(--gold)"/>
    <circle role="img" aria-label="Photo of a modern kitchen with white island" cx="360" cy="363" r="104" fill="url(#roundTone)"/>
    <circle cx="579" cy="425" r="102" fill="var(--gold)"/>
    <circle role="img" aria-label="Photo of a living room with city view windows" cx="579" cy="425" r="96" fill="url(#roundTone)"/>
    <!-- bottom strip -->
    <path d="M0,1010 L400,1010 L420,1020 L0,1020 Z" fill="var(--teal-soft)"/>
    <path d="M400,1010 L720,1010 L720,1020 L420,1020 Z" fill="var(--teal-deep)"/>
  </svg>

  <div class="brand-name">Kestrel Vale<br>Lodgings</div>

  <h1 class="headline">Furnished Apartments<br>Toronto, Stylish &amp;affordable Living</h1>

  <div class="services-pill">Our Management <strong>Services:</strong></div>

  <p class="service-cell cell-offering"><b class="label">Service Offering:</b> Clearly state that Kestrel Vale Lodgings specializes in property management services for condo owners in Toronto.</p>
  <p class="service-cell cell-fee"><b class="label">Fee Structure:</b> Highlight our competitive pricing model, which includes a management fee of <strong>15% plus tax</strong> of the pure rent we manage to secure for the property.</p>
  <p class="service-cell cell-marketing"><b class="label">Rental Marketing:</b> Emphasize our comprehensive approach to rental marketing by showcasing that we list the unit on our own website, as well as other booking engines such as Nestvora, QLMX, and other similar platforms (not limited to these).</p>
  <p class="service-cell cell-market"><b class="label">Target Market:</b> Emphasize that Kestrel Vale Lodgings specializes in securing one-month minimum executive rentals. However, highlight that we also manage units with short-term rental (STR) permits and can effectively market their properties for durations shorter than one month.</p>

  <div class="contact-tab">Contact Information</div>

  <div class="contact-phone">
    <svg width="20" height="20" viewBox="0 0 24 24" aria-hidden="true"><circle cx="12" cy="12" r="10.5" fill="none" stroke="currentColor" stroke-width="2"/><path d="M8.3 6.5l2 .2.8 2.6-1.3 1a7 7 0 0 0 3.9 3.9l1-1.3 2.6.8.2 2c-4.8.8-10-4.4-9.2-9.2z" fill="currentColor"/></svg>
    877-555-0142
  </div>

  <div class="contact-lines">
    <span><svg width="14" height="14" viewBox="0 0 24 24" aria-hidden="true"><circle cx="12" cy="12" r="10" fill="none" stroke="#222" stroke-width="2"/><ellipse cx="12" cy="12" rx="4.5" ry="10" fill="none" stroke="#222" stroke-width="2"/><line x1="2" y1="12" x2="22" y2="12" stroke="#222" stroke-width="2"/></svg>www.kestrelvalelodgings.example</span>
    <span><svg width="15" height="12" viewBox="0 0 24 18" aria-hidden="true"><rect x="1" y="1" width="22" height="16" fill="none" stroke="#222" stroke-width="2"/><path d="M1 1l11 9 11-9" fill="none" stroke="#222" stroke-width="2"/></svg>info@kestrelvalelodgings.example</span>
  </div>
</main>
</body>
</html>
```